TALL WAVE

I am in this industry for last 15 years we have done lots of commercial site like we work with ORBEL costruction, loam properties, DRV, quill construction.
We do all domestic and commercial wall and floor tiling, swimming pools, spas, paving, marbles blue stones and muchmore.

Specializing in the wall and floor Tiling, Waterproofing and floor preparations

Industry/Entity Type

Industry

Number of Pages Required

1 page

Font styles to use
Serif
Decorative

Colors

Designer to choose colors to be used in the design.

Requirements
Must have
• domestic and commercial indoor tiling, bathroom tiling and paving pictures
Nice to have
• beautiful bathroom pictures with tile

```html
<!DOCTYPE html>
<html lang="en">
<head>
<meta charset="utf-8">
<title>Tall Wave — Wall &amp; Floor Tiling</title>
<link href="https://fonts.googleapis.com/css2?family=Lato:wght@400;700;900&family=Open+Sans:wght@400;600;700&display=swap" rel="stylesheet">
<style>
:root{
  --orange:#e8793a;
  --ink:#1e1e1e;
  --body:#6b6b6b;
  --rule:#d6d6d6;
  --footer:#2b2b2b;
  --footer-line:#444;
  --white:#fff;
}
*{box-sizing:border-box;margin:0;padding:0}
html,body{width:1200px;height:3529px;overflow:hidden;background:var(--white)}
body{position:relative;font-family:"Open Sans",Arial,sans-serif;color:var(--body)}
.abs{position:absolute}
.heading{font-family:"Lato",Arial,sans-serif;font-weight:900;color:var(--ink);text-transform:uppercase}
.center{left:0;width:1200px;text-align:center}
.btn-solid{background:var(--orange);color:var(--white);font-family:"Lato",sans-serif;font-weight:700;font-size:15px;text-transform:uppercase;border-radius:26px;display:flex;align-items:center;justify-content:center;letter-spacing:.5px}
.btn-outline{border:2px solid #e3c1ad;color:var(--orange);font-family:"Lato",sans-serif;font-weight:700;font-size:12px;text-transform:uppercase;border-radius:20px;display:flex;align-items:center;justify-content:center}

/* hero */
.hero{left:0;top:0;width:1200px;height:541px;background:linear-gradient(90deg,#7d93a6 0%,#5c5f63 30%,#3d3e40 60%,#4a4845 100%)}
.hero-shade{left:0;top:0;width:1200px;height:541px;background:rgba(0,0,0,.18)}
.topbar{right:100px;top:20px;color:var(--white);font-size:14px;display:flex;gap:12px;align-items:center}
.topbar svg{vertical-align:middle;margin-right:6px}
.brand{left:99px;top:44px;display:flex;align-items:center;gap:14px;color:var(--white);font-family:"Lato",sans-serif;font-weight:700;font-size:24px}
.brand-mark{width:42px;height:42px;border:4px solid var(--white)}
.nav{left:414px;top:64px;display:flex;gap:30px;font-family:"Lato",sans-serif;font-weight:700;font-size:15px;color:var(--white);text-transform:uppercase}
.nav .active{color:var(--orange)}
.hero-title{top:168px;font-family:"Lato",sans-serif;font-weight:900;font-size:84px;letter-spacing:12px;color:var(--white)}
.hero-sub{top:268px;font-size:22px;font-weight:600;color:var(--white)}
.dots{display:flex;gap:4px}
.dots span{width:12px;height:12px;border-radius:50%;border:2px solid var(--white)}
.dots span.on{background:var(--white)}
.dots.dark span{border-color:#999}
.dots.dark span.on{background:#999}

/* welcome */
.welcome-title{left:99px;top:634px;font-size:32px}
.welcome-text{left:99px;width:440px;font-size:13px;line-height:24px}
.video-frame{left:581px;top:607px;width:471px;height:311px;border:2px solid #f0c7ae}
.video{left:609px;top:645px;width:480px;height:306px;background:linear-gradient(120deg,#d8d6d0,#a9aba7 55%,#8d8f8d)}
.play{left:817px;top:770px;width:60px;height:60px;border-radius:50%;border:3px solid var(--white);background:rgba(0,0,0,.3)}
.rule{left:99px;width:1002px;height:1px;background:var(--rule)}

/* services */
.section-title{font-size:31px}
.grid{left:99px;top:1198px;width:1002px;height:301px}
.cell{position:absolute;width:167px;height:150px}
.photo-a{background:linear-gradient(135deg,#3a3a3a,#8a8d90)}
.photo-b{background:linear-gradient(135deg,#8a9a8f,#4c5c4f)}
.photo-c{background:linear-gradient(135deg,#7c8a6f,#a6a58a)}
.photo-pool{background:linear-gradient(180deg,#3fb2d6,#1a7fb3)}
.photo-stone{background:linear-gradient(135deg,#cfc58a,#8d9060)}
.photo-dark{background:linear-gradient(135deg,#58524a,#1d1c1a)}
.service{position:absolute;width:167px;height:176px;background:var(--orange);color:var(--white);text-align:center;display:flex;flex-direction:column;justify-content:center}
.service.down{clip-path:polygon(0 0,100% 0,100% 86%,50% 100%,0 86%);padding-bottom:16px}
.service.up{clip-path:polygon(0 14%,50% 0,100% 14%,100% 100%,0 100%);padding-top:16px}
.service h3{font-family:"Lato",sans-serif;font-weight:700;font-size:19px;line-height:26px}
.service p{font-size:11px;font-style:italic;line-height:22px;margin-top:8px}

/* consult */
.consult{left:0;top:1605px;width:1200px;height:336px;background:linear-gradient(90deg,#8c8985,#6e6c69 50%,#545250)}
.consult-shade{left:0;top:1605px;width:1200px;height:336px;background:rgba(0,0,0,.3)}
.consult-title{top:1670px;font-family:"Lato",sans-serif;font-weight:900;font-size:30px;color:var(--white)}
.consult-text{top:1728px;left:230px;width:740px;text-align:center;font-size:14px;line-height:26px;color:#eee}

/* news */
.news-img{width:313px;height:219px}
.news-title{font-family:"Lato",sans-serif;font-weight:700;font-size:19px;color:var(--ink)}
.news-meta{font-size:12px;display:flex;gap:10px;align-items:center}
.news-meta svg{margin-right:5px;vertical-align:-2px}
.news-text{width:313px;font-size:12px;line-height:22px}

/* gallery */
.gallery-img{top:2802px;width:297px;height:205px}

/* footer */
.footer{left:0;top:3158px;width:1200px;height:371px;background:var(--footer)}
.footer-brand{left:99px;top:3297px;display:flex;align-items:center;gap:14px;color:var(--white);font-family:"Lato",sans-serif;font-weight:700;font-size:24px}
.footer h4{position:absolute;font-family:"Lato",sans-serif;font-weight:700;font-size:16px;color:var(--white);text-transform:uppercase;top:3238px}
.footer-links{left:407px;top:3277px;font-size:12px;line-height:25px;color:#ddd;list-style:none}
.footer-copy{font-size:12px;color:#ddd;line-height:22px}
.email-field{left:591px;top:3330px;width:255px;height:36px;border:1px solid #999;font-size:11px;color:#ddd;padding:10px 12px}
.subscribe{left:591px;top:3385px;width:104px;height:30px;border:2px solid var(--orange);border-radius:16px;color:var(--orange);font-size:11px;font-weight:700;text-transform:uppercase;display:flex;align-items:center;justify-content:center}
.contact-row{left:913px;font-size:12px;color:#ddd;line-height:20px;display:flex;gap:16px}
.footer-rule{left:99px;top:3450px;width:1002px;height:1px;background:var(--footer-line)}
.social{left:975px;top:3474px;display:flex;gap:8px}
.social span{width:26px;height:26px;border:1px solid #bbb;border-radius:50%}
</style>
</head>
<body>

<!-- Hero -->
<div class="abs hero" role="img" aria-label="Modern bathroom with dark grey wall tiles, freestanding bath and plants"></div>
<div class="abs hero-shade"></div>
<div class="abs topbar">
  <span><svg width="14" height="14" viewBox="0 0 24 24"><path fill="#e8793a" d="M6.6 10.8a15 15 0 006.6 6.6l2.2-2.2c.3-.3.7-.4 1-.2 1.1.4 2.3.6 3.6.6.6 0 1 .4 1 1V20c0 .6-.4 1-1 1A17 17 0 013 4c0-.6.4-1 1-1h3.5c.6 0 1 .4 1 1 0 1.3.2 2.5.6 3.6.1.3 0 .7-.2 1z"/></svg>1 555 014 2290</span>
  <span>|</span>
  <span><svg width="14" height="12" viewBox="0 0 24 20"><rect x="1" y="1" width="22" height="18" fill="#e8793a"/><path d="M1 2l11 8 11-8" fill="none" stroke="#fff" stroke-width="2"/></svg>info@tallwave.com</span>
</div>
<div class="abs brand"><span class="brand-mark"></span>TALL WAVE</div>
<nav class="abs nav">
  <span class="active">Home</span><span>About Us</span><span>Services</span><span>Project Gallery</span><span>News</span><span>Contact</span>
  <svg width="15" height="15" viewBox="0 0 24 24"><circle cx="10" cy="10" r="7" fill="none" stroke="#fff" stroke-width="3"/><path d="M15 15l7 7" stroke="#fff" stroke-width="3"/></svg>
</nav>
<h1 class="abs center hero-title">TALL WAVE</h1>
<p class="abs center hero-sub">We are Specialising in the wall and floor Tiling, Waterproofing and floor preparations</p>
<div class="abs btn-solid" style="left:510px;top:326px;width:180px;height:50px">Get a Quote</div>
<div class="abs dots" style="left:570px;top:472px"><span class="on"></span><span></span><span></span><span></span></div>

<!-- Welcome -->
<h2 class="abs heading welcome-title">Welcome to Tall Wave</h2>
<p class="abs welcome-text" style="top:700px">Nemo enim ipsam voluptatem quia voluptas sit aspernatur aut odit aute fugit, sed quia consequuntur magni dolo</p>
<p class="abs welcome-text" style="top:776px">Res eos qui ratione voluptatem sequi nesciunt. Neque porro quisquaest qui dolorem ipsum quia dolor sit amet, consectetur, adipisci velit, sedua non numquam eius modi tempora incidunt ut labore et quis nostruexerc itationem ullam corporis susem vel eum.</p>
<div class="abs btn-outline" style="left:99px;top:912px;width:132px;height:38px">Read More &gt;&gt;</div>
<div class="abs video-frame"></div>
<div class="abs video" role="img" aria-label="Bright bathroom with glass shower, vanity and stone tiles"></div>
<div class="abs play"><svg width="54" height="54" viewBox="0 0 54 54"><path d="M22 17l16 10-16 10z" fill="#fff"/></svg></div>
<div class="abs rule" style="top:1033px"></div>

<!-- What we do -->
<h2 class="abs heading center section-title" style="top:1105px">What We Do</h2>
<div class="abs grid">
  <div class="cell photo-a" style="left:0;top:0" role="img" aria-label="Tiled bathroom wall"></div>
  <div class="cell photo-b" style="left:334px;top:0" role="img" aria-label="Indoor spa pool"></div>
  <div class="cell photo-c" style="left:668px;top:0" role="img" aria-label="Outdoor stone paving"></div>
  <div class="cell photo-pool" style="left:167px;top:151px" role="img" aria-label="Blue swimming pool tiles"></div>
  <div class="cell photo-stone" style="left:501px;top:151px" role="img" aria-label="Pebble paving floor"></div>
  <div class="cell photo-dark" style="left:835px;top:151px" role="img" aria-label="Dark tiled floor with lights"></div>

  <div class="service down" style="left:167px;top:0"><h3>Swimming<br>pools</h3><p>Domestic &amp; commercial<br>indoor tiling</p></div>
  <div class="service down" style="left:501px;top:0"><h3>Paving<br>Floor</h3><p>Domestic &amp; commercial<br>indoor tiling</p></div>
  <div class="service down" style="left:835px;top:0"><h3>View<br>More</h3><p>Domestic &amp; commercial<br>indoor tiling</p></div>
  <div class="service up" style="left:0;top:125px"><h3>Wall &amp;<br>Floor Tiling</h3><p>Domestic &amp; commercial<br>indoor tiling</p></div>
  <div class="service up" style="left:334px;top:125px"><h3>Spas<br>Tiling</h3><p>Domestic &amp; commercial<br>indoor tiling</p></div>
  <div class="service up" style="left:668px;top:125px"><h3>Marbles blue<br>stones</h3><p>Domestic &amp; commercial<br>indoor tiling</p></div>
</div>

<!-- Consultation -->
<div class="abs consult" role="img" aria-label="Bathroom with white basin, freestanding bath and large grey floor tiles"></div>
<div class="abs consult-shade"></div>
<h2 class="abs center consult-title">GET FREE CONSULTATION</h2>
<p class="abs consult-text">Sed ut perspiciatis unde omnis iste natus error sit voluptatem accusantium doloremque laudantium, totam rem aperiam, eaque ipsa quae ab illo inventore veritatis et quasi architecto beatae vitae dicta.</p>
<div class="abs btn-solid" style="left:510px;top:1807px;width:180px;height:48px">Get Started</div>

<!-- Latest news -->
<h2 class="abs heading center section-title" style="top:2015px">Latest News</h2>

<div class="abs news-img" style="left:99px;top:2111px;background:linear-gradient(135deg,#e8e2d6,#b9ab93)" role="img" aria-label="Open living room with polished floor tiles"></div>
<div class="abs news-img" style="left:442px;top:2111px;background:linear-gradient(135deg,#9aa07e,#6b6f55)" role="img" aria-label="Tradesman laying stone paving beside a stone wall"></div>
<div class="abs news-img" style="left:788px;top:2111px;background:linear-gradient(135deg,#c9c3b8,#8f887c)" role="img" aria-label="Tiler spreading adhesive on a wall"></div>

<h3 class="abs news-title" style="left:99px;top:2353px">Finibus Bonorum Llanditet Ma</h3>
<h3 class="abs news-title" style="left:442px;top:2353px">Finibus Bonorum Llanditet Ma</h3>
<h3 class="abs news-title" style="left:788px;top:2353px">Finibus Bonorum Llanditet Ma</h3>

<div class="abs news-meta" style="left:99px;top:2393px"><span><svg width="12" height="12" viewBox="0 0 12 12"><rect x="1" y="2" width="10" height="9" fill="none" stroke="#e8793a" stroke-width="1.5"/><path d="M1 5h10" stroke="#e8793a"/></svg>02/08/2017</span><span>|</span><span><svg width="12" height="12" viewBox="0 0 12 12"><circle cx="6" cy="4" r="3" fill="#e8793a"/><path d="M1 12a5 5 0 0110 0z" fill="#e8793a"/></svg>Sam Reed</span></div>
<div class="abs news-meta" style="left:442px;top:2393px"><span><svg width="12" height="12" viewBox="0 0 12 12"><rect x="1" y="2" width="10" height="9" fill="none" stroke="#e8793a" stroke-width="1.5"/><path d="M1 5h10" stroke="#e8793a"/></svg>02/08/2017</span><span>|</span><span><svg width="12" height="12" viewBox="0 0 12 12"><circle cx="6" cy="4" r="3" fill="#e8793a"/><path d="M1 12a5 5 0 0110 0z" fill="#e8793a"/></svg>Sam Reed</span></div>
<div class="abs news-meta" style="left:788px;top:2393px"><span><svg width="12" height="12" viewBox="0 0 12 12"><rect x="1" y="2" width="10" height="9" fill="none" stroke="#e8793a" stroke-width="1.5"/><path d="M1 5h10" stroke="#e8793a"/></svg>02/08/2017</span><span>|</span><span><svg width="12" height="12" viewBox="0 0 12 12"><circle cx="6" cy="4" r="3" fill="#e8793a"/><path d="M1 12a5 5 0 0110 0z" fill="#e8793a"/></svg>Sam Reed</span></div>

<p class="abs news-text" style="left:99px;top:2428px">Nam libero tempore, cum soluta nobis est eligendi optio cumque nihil impedit quo minus id quod ma oxime placeat facere possimus.</p>
<p class="abs news-text" style="left:442px;top:2428px">Nam libero tempore, cum soluta nobis est eligendi optio cumque nihil impedit quo minus id quod ma oxime placeat facere possimus.</p>
<p class="abs news-text" style="left:788px;top:2428px">Nam libero tempore, cum soluta nobis est eligendi optio cumque nihil impedit quo minus id quod ma oxime placeat facere possimus.</p>

<div class="abs btn-outline" style="left:99px;top:2516px;width:113px;height:35px">Read More</div>
<div class="abs btn-outline" style="left:442px;top:2516px;width:113px;height:35px">Read More</div>
<div class="abs btn-outline" style="left:788px;top:2516px;width:113px;height:35px">Read More</div>

<div class="abs rule" style="top:2647px"></div>

<!-- Project gallery -->
<h2 class="abs heading center section-title" style="top:2717px">Project Gallery</h2>
<div class="abs gallery-img" style="left:0;background:linear-gradient(135deg,#4f6f8f,#5d5a56)" role="img" aria-label="Blue bathroom with stone feature wall"></div>
<div class="abs gallery-img" style="left:301px;background:linear-gradient(135deg,#d9d5cc,#7a5a45)" role="img" aria-label="Living room with vaulted ceiling and brick wall"></div>
<div class="abs gallery-img" style="left:602px;background:linear-gradient(135deg,#f0eeea,#b5aea3)" role="img" aria-label="White kitchen with tiled floor"></div>
<div class="abs gallery-img" style="left:903px;width:297px;background:linear-gradient(135deg,#6b5540,#c9b89e)" role="img" aria-label="Hallway with polished concrete floor"></div>
<div class="abs" style="left:120px;top:2877px;width:50px;height:50px;border-radius:50%;border:2px solid #fff;background:rgba(0,0,0,.3)"><svg width="46" height="46" viewBox="0 0 46 46"><path d="M23 14v18M14 23h18" stroke="#fff" stroke-width="3"/></svg></div>
<div class="abs dots dark" style="left:578px;top:3048px"><span class="on"></span><span></span><span></span></div>

<!-- Footer -->
<footer class="abs footer"></footer>
<div class="abs footer-brand"><span class="brand-mark"></span>TALL WAVE</div>
<div class="footer">
  <h4 style="left:407px">Quick Links</h4>
  <h4 style="left:591px">Newsletter Subscription</h4>
  <h4 style="left:913px">Contact Us</h4>
</div>
<ul class="abs footer-links">
  <li>Home</li><li>About Us</li><li>Services</li><li>Project Gallery</li><li>News</li><li>Contact</li>
</ul>
<p class="abs footer-copy" style="left:591px;top:3278px;width:260px">Register your Email Address to get information about us</p>
<div class="abs email-field">Email Address</div>
<div class="abs subscribe">Subscribe</div>
<div class="abs contact-row" style="top:3282px"><svg width="12" height="14" viewBox="0 0 12 16"><path d="M6 0a6 6 0 016 6c0 4-6 10-6 10S0 10 0 6a6 6 0 016-6z" fill="#e8793a"/><circle cx="6" cy="6" r="2" fill="#2b2b2b"/></svg><span>12 Ferncliff Rd, Lower<br>Brookvale</span></div>
<div class="abs contact-row" style="top:3346px"><svg width="12" height="12" viewBox="0 0 24 24"><path fill="#e8793a" d="M6.6 10.8a15 15 0 006.6 6.6l2.2-2.2c.3-.3.7-.4 1-.2 1.1.4 2.3.6 3.6.6.6 0 1 .4 1 1V20c0 .6-.4 1-1 1A17 17 0 013 4c0-.6.4-1 1-1h3.5c.6 0 1 .4 1 1 0 1.3.2 2.5.6 3.6.1.3 0 .7-.2 1z"/></svg><span>1 555 014 2290</span></div>
<div class="abs contact-row" style="top:3390px"><svg width="12" height="10" viewBox="0 0 24 20"><rect x="1" y="1" width="22" height="18" fill="#e8793a"/><path d="M1 2l11 8 11-8" fill="none" stroke="#2b2b2b" stroke-width="2"/></svg><span>info@tallwave.com</span></div>
<div class="abs footer-rule"></div>
<p class="abs footer-copy" style="left:99px;top:3476px">Copyrights © 2017, Tall Wave. All rights reserved.</p>
<div class="abs social"><span></span><span></span><span></span><span></span></div>

</body>
</html>
```